Création d'un modèle de compte-rendus
Besoins
Cabinet de recrutement et de conseil en Ressources Humaines, nous intervenons depuis plus de 60 ans auprès d’entreprises afin de pourvoir leurs besoins en recrutement.
Nous intervenons sur tout type de postes, du cadre dirigeant à l’ouvrier, avec une majorité de postes à responsabilités.
Dans le cadre de nos recrutements, nous envoyons à l’entreprise cliente un document de synthèse des candidats intéressants que nous rencontrons. Dans ce document, nous présentons son parcours professionnel, ses informations générales (mobilité, préavis, rémunération…), ses principaux traits de personnalité, son potentiel intellectuel ainsi qu’une conclusion présentant les points forts, les axes de progrès et notre avis sur ce candidat.
Nos synthèses actuelles sont sous la forme d’un document WORD de 4 à 6 pages assez classique et nous souhaiterions avoir un document plus dynamique, tout en restant sobre. Les informations clés doivent être rapides à identifier et accessibles à l’œil facilement.
La cible :
Directeurs Généraux, Directeurs des Ressources Humaines, Responsable Recrutement
Tous secteurs d’activité
Groupes internationaux, Entreprises/Industries nationales ou locales, PME/PMI
Couleurs, favoris et autres exigences :
Cf notre logo et site internet : www.travenor-exemple.fr, tons bleus et blancs principalement
Sobriété, Simplicité
Nous sommes ouverts à toute proposition créative de votre part.

```html
<!DOCTYPE html>
<html lang="fr">
<head>
<meta charset="UTF-8">
<title>Fiche candidat – Travenor Conseil</title>
<link href="https://fonts.googleapis.com/css2?family=Lato:wght@300;400&display=swap" rel="stylesheet">
<style>
  :root {
    --blue: #1a62a0;
    --brand-blue: #2f74ad;
    --light-grey: #d6d7dc;
    --plum: #8a3362;
    --white: #ffffff;
    --tagline-grey: #9a9ca3;
    --photo-dark: #3a3d44;
    --photo-mid: #6b7480;
    --photo-light: #a9b6c4;
  }
  html, body {
    margin: 0;
    padding: 0;
    overflow: hidden;
    background: var(--white);
  }
  .cover {
    position: relative;
    width: 848px;
    height: 1200px;
    overflow: hidden;
    background: var(--white);
    font-family: "Lato", sans-serif;
  }
  .cover-shapes {
    position: absolute;
    inset: 0;
    display: block;
  }
  .doc-title {
    position: absolute;
    left: 296px;
    top: 92px;
    width: 256px;
    height: 72px;
    box-sizing: border-box;
    border: 1px dashed rgba(255, 255, 255, 0.75);
    display: flex;
    align-items: center;
    justify-content: center;
    color: var(--white);
    font-weight: 300;
    font-size: 21px;
    letter-spacing: 0.5px;
  }
  .brand {
    position: absolute;
    left: 0;
    right: 0;
    top: 950px;
    text-align: center;
    margin-left: 90px;
  }
  .brand-name {
    margin: 0;
    color: var(--brand-blue);
    font-weight: 400;
    font-size: 40px;
    line-height: 1;
    display: inline-block;
    padding-bottom: 6px;
    border-bottom: 1px solid var(--brand-blue);
  }
  .brand-tagline {
    margin: 6px 0 0;
    color: var(--tagline-grey);
    font-weight: 400;
    font-size: 13.5px;
    letter-spacing: 1px;
  }
</style>
</head>
<body>
<main class="cover">
  <svg class="cover-shapes" width="848" height="1200" viewBox="0 0 600 848" aria-hidden="false">
    <defs>
      <linearGradient id="photo-tone" x1="0" y1="0" x2="1" y2="0.3">
        <stop offset="0" stop-color="var(--photo-dark)"/>
        <stop offset="0.45" stop-color="var(--photo-mid)"/>
        <stop offset="1" stop-color="var(--photo-light)"/>
      </linearGradient>
    </defs>
    <polygon class="band-blue" fill="var(--blue)" points="0,0 600,0 600,112 300,222 0,110"/>
    <polygon class="wedge-grey-left" fill="var(--light-grey)" points="0,110 300,222 0,335"/>
    <polygon class="photo-band" role="img"
      aria-label="Photographie : homme d'affaires en costume tenant dans sa main un globe terrestre relié par un réseau de contacts"
      fill="url(#photo-tone)" points="0,347 600,118 600,402 0,640"/>
    <polygon class="wedge-grey-right" fill="var(--light-grey)" points="322,520 600,416 600,612"/>
    <polygon class="wedge-plum" fill="var(--plum)" points="470,700 600,588 600,822"/>
  </svg>

  <div class="doc-title">FICHE CANDIDAT</div>

  <div class="brand">
    <p class="brand-name">Travenor Conseil</p>
    <p class="brand-tagline">Recrutement &amp; Ressources Humaines</p>
  </div>
</main>
</body>
</html>
```